Premium Organic Ceremonial Matcha Green Tea - Product Label

Two Label Bag Sizes: 18x30cm and 17x24cm

Be EXTRA Creative.. please message me with any questions and I will respond quickly.

Target Market(s)

Health, Organic, Green Tea Matcha Drinkers

Industry/Entity Type

Product

Requirements
Must have
• Organic Matcha Green Tea
• Try to incorporate geometry in logo into design... not mandatory but preferred for branding.

```html
<!DOCTYPE html>
<html lang="en">
<head>
<meta charset="utf-8">
<title>Verdant Grove – Organic Matcha Green Tea Labels</title>
<link rel="stylesheet" href="https://fonts.googleapis.com/css2?family=Damion&family=Montserrat:wght@500;700&display=swap">
<style>
  :root {
    --canvas: #ffffff;
    --label-cream: #ecefe2;
    --leaf-deep: #3f8f4f;
    --leaf-mid: #5aa866;
    --leaf-light: #9fd3a6;
    --title-green: #6db27b;
    --script-ink: #3a3a3a;
    --brand-green: #6a9a4a;
    --back-green: #5fc27a;
    --back-pale: #e4f1e2;
  }
  * { margin: 0; padding: 0; box-sizing: border-box; }
  html, body {
    width: 1200px; height: 890px; overflow: hidden;
    background: var(--canvas);
  }
  .canvas {
    position: relative; width: 1200px; height: 890px;
  }
  .label {
    position: absolute; overflow: hidden; border-radius: 6px;
  }
  .label--front {
    left: 290px; top: 235px; width: 330px; height: 510px;
    background: var(--label-cream);
  }
  .label--back {
    left: 660px; top: 135px; width: 330px; height: 510px;
    background: radial-gradient(circle at 50% 52%, var(--back-pale) 0 70px, var(--leaf-light) 120px, var(--back-green) 230px, var(--leaf-light) 330px);
  }
  .leaf-band {
    position: absolute; left: 30px; width: 270px; height: 130px;
  }
  .leaf-band--top {
    top: 0;
    border-radius: 0 0 135px 135px;
    background: radial-gradient(ellipse at 50% 0%, var(--leaf-deep), var(--leaf-mid) 60%, var(--leaf-light));
  }
  .leaf-band--bottom {
    bottom: 0;
    border-radius: 135px 135px 0 0;
    background: radial-gradient(ellipse at 50% 100%, var(--leaf-deep), var(--leaf-mid) 60%, var(--leaf-light));
  }
  .brand {
    position: absolute; left: 0; right: 0;
    text-align: center;
    font-family: "Montserrat", sans-serif; font-weight: 500;
    font-size: 15px; color: var(--brand-green); letter-spacing: 0.5px;
  }
  .label--front .brand { top: 228px; }
  .label--back .brand { top: 263px; }
  .title {
    position: absolute; left: 0; right: 0; top: 262px; text-align: center;
  }
  .title__script {
    display: block;
    font-family: "Damion", cursive; font-size: 44px; line-height: 1;
    color: var(--script-ink);
  }
  .title__main {
    display: block; margin-top: 8px;
    font-family: "Montserrat", sans-serif; font-weight: 700;
    font-size: 44px; line-height: 1; letter-spacing: 1px;
    color: var(--title-green);
  }
</style>
</head>
<body>
<main class="canvas">
  <section class="label label--back" role="img" aria-label="Back label: overlapping green leaf petals forming a wreath around a pale centre">
    <p class="brand">Verdant Grove</p>
  </section>

  <section class="label label--front">
    <div class="leaf-band leaf-band--top" role="img" aria-label="Green leaf petal rosette at the top edge"></div>
    <p class="brand">Verdant Grove</p>
    <h1 class="title">
      <span class="title__script">Organic Matcha</span>
      <span class="title__main">GREEN TEA</span>
    </h1>
    <div class="leaf-band leaf-band--bottom" role="img" aria-label="Green leaf petal rosette at the bottom edge"></div>
  </section>
</main>
</body>
</html>
```